ALL ASPECTS OF PLASTERING INC: TEXTURE,SANDFINISH RENO,POOLS, PATCH WORK ( STATEWIDE SERVICE GOOD RATES) 100% GUARANTEED FULLY INSURED C

Target Market(s)

ANYONE WHO OWNS A HOUSE,BUILDERS

Industry/Entity Type

Work

Contact Information for Business Card

KLAY-TOPP PLASTERING SERVICES
GERALD PETRAKIS 0438916247
EMAIL:VORTAKE58@QUENMAIL.COM

Requirements
Must have
• COLOUR BACKGROUND WIV PLASTERING PICTURE EG TROWEL, CEMENT MIXER, SAND
Nice to have
• BOLD PROFESSIONAL LOOKING AND SOUNDING CATCHY SAYING
Should not have
• FLURO COLOURS

```html
<!DOCTYPE html>
<html lang="en">
<head>
<meta charset="utf-8">
<title>Klay-Topp Plastering Services – Business Card</title>
<link rel="stylesheet" href="https://fonts.googleapis.com/css2?family=Dosis:wght@200;300;400;500;600;800&display=swap">
<style>
  :root {
    --page: #ffffff;
    --card-base: #f6e9e2;
    --card-band: #f0ddd3;
    --card-light: #fbf3ec;
    --ink: #0b0b0b;
    --ink-soft: #555555;
    --brick: #9a2a27;
    --cream: #f7ece1;
  }
  * { box-sizing: border-box; margin: 0; padding: 0; }
  html, body {
    width: 1200px; height: 1000px; overflow: hidden;
    background: var(--page);
    font-family: "Dosis", sans-serif;
  }
  .canvas { position: relative; width: 1200px; height: 1000px; }

  .card {
    position: absolute;
    width: 665px; height: 410px;
    overflow: hidden;
    background:
      linear-gradient(90deg, rgba(255,255,255,0.55) 0%, rgba(255,255,255,0) 12%, rgba(255,255,255,0) 88%, rgba(255,255,255,0.55) 100%),
      repeating-linear-gradient(180deg,
        var(--card-light) 0 45px,
        var(--card-base) 45px 115px,
        var(--card-band) 115px 160px,
        var(--card-light) 160px 182px,
        var(--card-base) 182px 250px);
  }

  /* Contact side */
  .card--contact { left: 463px; top: 147px; }
  .business-name {
    position: absolute; left: 46px; top: 52px;
    color: var(--ink); font-weight: 500; line-height: 1.1;
  }
  .business-name__main { display: block; font-size: 60px; letter-spacing: 1px; }
  .business-name__trade { display: block; font-size: 30px; margin-top: 4px; margin-left: 10px; }

  .contact { position: absolute; right: 52px; top: 266px; text-align: right; color: var(--ink); font-style: normal; line-height: 1.2; }
  .contact__name { font-size: 28px; font-weight: 500; letter-spacing: 0.5px; }
  .contact__phone { font-size: 21px; font-weight: 300; margin-top: 2px; letter-spacing: 0.5px; }
  .contact__email { font-size: 20px; font-weight: 300; margin-top: 2px; }

  /* Slogan side */
  .card--slogan { left: 67px; top: 447px; }
  .slogan { position: absolute; inset: 0; }
  .slogan > span { position: absolute; line-height: 1; }
  .slogan__we { left: 50px; top: 52px; font-size: 68px; font-weight: 200; color: var(--ink-soft); }
  .slogan__cover { left: 147px; top: 82px; font-size: 46px; font-weight: 300; color: var(--brick); }
  .slogan__all { left: 116px; top: 132px; font-size: 68px; font-weight: 800; color: var(--ink); }
  .slogan__aspects { left: 190px; top: 196px; font-size: 36px; font-weight: 200; color: var(--ink-soft); }
  .slogan__trade {
    left: 260px; top: 242px; width: 359px; height: 112px;
    background: var(--ink); color: var(--cream);
    font-size: 76px; font-weight: 600; line-height: 104px; text-align: center; letter-spacing: 1px;
  }

  .seal { position: absolute; left: 33px; top: 233px; width: 140px; height: 140px; }
</style>
</head>
<body>
<main class="canvas">

  <section class="card card--contact" aria-label="Business card, contact side">
    <h1 class="business-name">
      <span class="business-name__main">Klay-Topp</span>
      <span class="business-name__trade">Plastering Services</span>
    </h1>
    <address class="contact">
      <div class="contact__name">Gerald Petrakis</div>
      <div class="contact__phone">0438 916 247</div>
      <div class="contact__email">Vortake58@quenmail.com</div>
    </address>
  </section>

  <section class="card card--slogan" aria-label="Business card, slogan side">
    <div class="slogan">
      <span class="slogan__we">We</span>
      <span class="slogan__cover">cover</span>
      <span class="slogan__all">ALL</span>
      <span class="slogan__aspects">aspects of</span>
      <span class="slogan__trade">plastering</span>
    </div>
    <svg class="seal" viewBox="0 0 140 140" role="img" aria-label="Guarantee seal">
      <circle cx="70" cy="70" r="68" fill="var(--brick)"/>
    </svg>
  </section>

</main>
</body>
</html>
```